The Pixel Tap Business card.

A Simple card with our Logo and contact information. To give to investors and other professionals.

We are a nerd themed bar.
our target market is young professionals age 21+ but the real purpose of this business card is to present to potential investors and other professionals with our contact information. as we are still looking for funding before we start up.

I am partial to green and my partner likes red we are open to iteration.

Target Market(s)

Investors

Industry/Entity Type

Business

Contact Information for Business Card

Martin Hale (225) 730-6192 kent.h4711@mailnest.test Glen Porter (225) 968-5037 glenp318@mailnest.test

Font styles to use
Serif

Requirements
Nice to have
• Keep it simple but not boring.
• Use the Logos but feel free to edit them to match theme/colors.
• Keep the back clean and use one of the Logos.

```html
<!DOCTYPE html>
<html lang="en">
<head>
<meta charset="utf-8">
<title>The Pixel Tap – Business Card</title>
<link rel="stylesheet" href="https://fonts.googleapis.com/css2?family=Fanwood+Text&display=swap">
<style>
  :root {
    --ink: #050505;
    --signal-red: #e52330;
    --paper: #ffffff;
  }
  html, body {
    margin: 0;
    padding: 0;
    width: 1200px;
    height: 342px;
    overflow: hidden;
    background: var(--paper);
  }
  .card-sheet {
    position: relative;
    width: 1200px;
    height: 342px;
    font-family: "Fanwood Text", Georgia, serif;
    color: var(--ink);
  }
  .card-front {
    position: absolute;
    left: 20px;
    top: 31px;
    width: 530px;
    height: 218px;
    display: flex;
    align-items: center;
    justify-content: center;
    gap: 18px;
  }
  .brand-dot {
    width: 44px;
    height: 44px;
    border-radius: 50%;
    background: var(--signal-red);
    flex: none;
  }
  .brand-name {
    margin: 0;
    font-size: 66px;
    font-weight: 400;
    line-height: 1;
    color: var(--ink);
    white-space: nowrap;
  }
  .card-back {
    position: absolute;
    left: 666px;
    top: 19px;
    width: 534px;
    height: 231px;
    background: var(--signal-red);
    display: flex;
    flex-direction: column;
    align-items: center;
    justify-content: center;
    gap: 26px;
    padding-left: 2px;
    box-sizing: border-box;
  }
  .contact {
    text-align: center;
    font-size: 27px;
    line-height: 25px;
    margin: 0;
  }
  .contact span { display: block; }
  .pixel-strip {
    position: absolute;
    top: 285px;
    height: 25px;
    width: 531px;
    display: flex;
    gap: 19px;
    overflow: hidden;
  }
  .pixel-strip--front { left: 19px; }
  .pixel-strip--back { left: 667px; width: 533px; }
  .pixel-strip i {
    display: block;
    flex: none;
    width: 31px;
    height: 25px;
    background: #000;
  }
</style>
</head>
<body>
<main class="card-sheet">
  <section class="card-front">
    <span class="brand-dot" aria-hidden="true"></span>
    <h1 class="brand-name">The Pixel Tap</h1>
  </section>

  <section class="card-back">
    <p class="contact">
      <span>Martin Hale (225) 730-6192</span>
      <span>kent.h4711@mailnest.test</span>
    </p>
    <p class="contact">
      <span>Glen Porter (225) 968-5037</span>
      <span>glenp318@mailnest.test</span>
    </p>
  </section>

  <div class="pixel-strip pixel-strip--front" aria-hidden="true">
    <i></i><i></i><i></i><i></i><i></i><i></i><i></i><i></i><i></i><i></i><i></i>
  </div>
  <div class="pixel-strip pixel-strip--back" aria-hidden="true">
    <i></i><i></i><i></i><i></i><i></i><i></i><i></i><i></i><i></i><i></i><i></i>
  </div>
</main>
</body>
</html>
```